Telecom Equipment datasheet, case study, and white paper templates

We have the need for a Microsoft Word template that can be printed to PDF directly, without the need for an Adobe software expert to produce product datasheets, case studies, and white papers. I envision the datasheet to be a superset of all templates, where case study is a subset of the total elements, and white paper has fewer of the elements, but all share the same overall design. We would like the datasheet to be 4 pages and have several sections including highlights, and efficient tables with a clean design.

Target Market(s)

Technical and business employees within telecommunications providers

Industry/Entity Type

Telecom

Font styles to use
Other font styles liked:
• Lato

Colors
34a6d7

Requirements
Must have
• Must follow the design guidelines document for colors and font (Lato). Sections of the datasheet include these, where taking sections out could allow for the same base template to serve as a case study or white paper. The product image should be white background, and while banners or borders are OK, they are not required if keeping the template very clean looking informs a more basic layout. The main goal is to have a template that is easy to use, even if it means sacrificing some production quality.
Nice to have
• Mostly white, easy to print, main color is Process Cyan C, though from the example image, using orange and yellow to imply light and motion are good (given our equipment moves data to and from the internet)
Should not have
• 15 pages like the example, 4 pages is all we need, making the table formatting (for the end of the template) a vital part of the design.

```html
<!DOCTYPE html>
<html lang="en">
<head>
<meta charset="utf-8">
<title>NXT Document Template Suite</title>
<link href="https://fonts.googleapis.com/css2?family=Lato:wght@400;700;900&display=swap" rel="stylesheet">
<style>
:root{
  --cyan:#34a6d7;
  --cyan-deep:#1f8cc8;
  --cyan-pale:#d4eaf7;
  --cyan-soft:#e9f4fb;
  --ink:#3b3f45;
  --ink-soft:#6b7077;
  --slate:#55595f;
  --stage:#e4e4e4;
  --paper:#ffffff;
}
*{box-sizing:border-box;margin:0;padding:0}
html,body{width:1200px;height:1200px;overflow:hidden;background:var(--stage);font-family:'Lato',Arial,sans-serif;color:var(--ink)}
.page{position:absolute;width:254px;height:358px;background:var(--paper);box-shadow:0 1px 4px rgba(0,0,0,.18);overflow:hidden}
.pg-title{position:absolute;left:26px;right:22px;top:24px;text-align:center;font-size:9px;letter-spacing:.2px;color:var(--ink);padding-bottom:3px;border-bottom:1px solid var(--cyan-pale)}
.content{position:absolute;left:26px;right:22px;top:48px}
.h2{font-size:6.4px;font-weight:700;color:var(--ink);margin:5px 0 2px}
.kicker{font-size:3.4px;color:var(--cyan);margin:3px 0 1px}
.body{font-size:3.3px;line-height:1.55;color:var(--ink)}
.body p{margin-bottom:3px}
.link{color:var(--cyan)}
.lead{font-size:5.6px;line-height:1.2;font-weight:700;color:var(--cyan-deep)}
.footer{position:absolute;left:26px;right:22px;bottom:15px;height:5px;display:flex;align-items:center;gap:3px}
.footer .url{flex:0 0 152px;height:3.5px;background:var(--slate);font-size:2.6px;color:#fff;line-height:3.5px;padding-left:3px;clip-path:polygon(0 0,100% 0,96% 100%,0 100%)}
.footer .mark{font-size:5.5px;font-weight:900;color:var(--slate);padding:0 2px}
.footer .num{flex:1;height:3.5px;background:var(--cyan);font-size:2.6px;color:#fff;line-height:3.5px;text-align:right;padding-right:8px;clip-path:polygon(4% 0,100% 0,100% 100%,0 100%)}
.photo{background:linear-gradient(135deg,#8fb6d6,#2f4f6e)}
table{border-collapse:separate;border-spacing:1px;width:100%}
.data td,.data th{font-size:3px;height:6px;padding:0 3px;text-align:left}
.data th{background:var(--slate);color:#fff;font-weight:700;text-align:center}
.data td{background:var(--cyan-pale)}
.data td.c{text-align:center}
.data tr.sub td{background:var(--cyan-soft);color:var(--cyan-deep);font-weight:700}
.data tr.total td{font-weight:700}
.data tr.grand td{background:var(--cyan);color:#fff;font-weight:700}
.grid td{border:0.5px solid #9fc9e8;height:7px;background:#fff}
.grid tr.head td{background:var(--cyan);border-color:var(--cyan)}
.grid tr:nth-child(even):not(.head) td{background:var(--cyan-soft)}
</style>
</head>
<body>

<!-- Cover -->
<section class="page" style="left:47px;top:36px">
  <div style="position:absolute;top:34px;left:0;right:0;text-align:center;font-size:34px;font-weight:900;color:var(--slate);letter-spacing:1px">NXT</div>
  <div role="img" aria-label="Abstract blue corridor of glowing tiles" style="position:absolute;top:88px;left:0;right:0;height:178px;background:radial-gradient(ellipse at 60% 45%,#8fd3f3 0%,#34a6d7 45%,#1c7fc0 100%)"></div>
  <div style="position:absolute;top:266px;left:0;right:0;height:8px;background:var(--slate)"></div>
  <div style="position:absolute;top:146px;left:27px;font-size:13px;line-height:1.45;font-weight:700;color:#fff">LOREM IPSUM IS SIMPLY<br>DUMMY HAS BEEN</div>
  <div style="position:absolute;top:294px;left:0;right:0;text-align:center;font-size:6.6px;font-weight:700;color:var(--ink)">LOREM IPSUM IS SIMPLY ETIAM VESTIBULUM</div>
</section>

<!-- Revision page -->
<section class="page" style="left:337px;top:36px">
  <table class="grid" style="position:absolute;top:44px;left:36px;width:184px;border-spacing:0">
    <tr><td style="font-size:3px;color:var(--cyan);width:28px">Version #</td><td style="font-size:3px;color:var(--cyan);width:78px">Purpose / Changes</td><td style="font-size:3px;color:var(--cyan);width:52px">Author</td><td style="font-size:3px;color:var(--cyan)">Date</td></tr>
    <tr><td></td><td style="background:#eee"></td><td></td><td></td></tr>
    <tr><td></td><td style="background:#eee"></td><td></td><td></td></tr>
    <tr><td></td><td style="background:#eee"></td><td></td><td></td></tr>
    <tr><td></td><td style="background:#eee"></td><td></td><td></td></tr>
    <tr><td></td><td style="background:#eee"></td><td></td><td></td></tr>
    <tr><td></td><td style="background:#eee"></td><td></td><td></td></tr>
  </table>
  <div aria-hidden="true" style="position:absolute;left:0;bottom:-14px;font-size:108px;font-weight:900;color:#f1f4f7;letter-spacing:4px">NXT</div>
  <div style="position:absolute;top:296px;left:72px;border-left:1.5px solid var(--cyan);padding-left:5px;font-size:3px;line-height:1.6;color:var(--ink-soft)">Copyright © 2018 Orbit Global Services Group.<br>All Rights Reserved.<br>No part of the contents of this document may be reproduced or distributed in any form or by<br>any means without the prior written permission of Orbit Global Services Group.</div>
</section>

<!-- Table of contents -->
<section class="page" style="left:628px;top:36px">
  <div class="pg-title">TABLE OF CONTENTS</div>
  <div class="content" style="top:52px">
    <div class="h2" style="margin-bottom:5px">Contents</div>
    <div class="body" style="font-size:3.2px;line-height:2.6">
      <div style="display:flex"><span>Table of Contents</span><span style="flex:1;border-bottom:0.5px dotted #999;margin:0 3px 2px"></span><span>01</span></div>
      <div style="display:flex"><span>Executive Summary</span><span style="flex:1;border-bottom:0.5px dotted #999;margin:0 3px 2px"></span><span>02</span></div>
      <div style="display:flex"><span>Our Understanding of Your Needs</span><span style="flex:1;border-bottom:0.5px dotted #999;margin:0 3px 2px"></span><span>02</span></div>
      <div style="display:flex"><span>Our Recommendations</span><span style="flex:1;border-bottom:0.5px dotted #999;margin:0 3px 2px"></span><span>03</span></div>
      <div style="display:flex"><span>Our Approach</span><span style="flex:1;border-bottom:0.5px dotted #999;margin:0 3px 2px"></span><span>05</span></div>
      <div style="display:flex"><span>Budget and Timeframe</span><span style="flex:1;border-bottom:0.5px dotted #999;margin:0 3px 2px"></span><span>07</span></div>
      <div style="display:flex"><span>Appendix A: About Marlow Creek</span><span style="flex:1;border-bottom:0.5px dotted #999;margin:0 3px 2px"></span><span>10</span></div>
      <div style="display:flex"><span>Appendix B: Selected Client List</span><span style="flex:1;border-bottom:0.5px dotted #999;margin:0 3px 2px"></span><span>10</span></div>
      <div style="display:flex"><span>Appendix C: Our Capabilities</span><span style="flex:1;border-bottom:0.5px dotted #999;margin:0 3px 2px"></span><span>11</span></div>
      <div style="display:flex"><span>Appendix D: Our Process</span><span style="flex:1;border-bottom:0.5px dotted #999;margin:0 3px 2px"></span><span>12</span></div>
    </div>
  </div>
  <div class="footer"><div class="url">www.website.com</div><div class="mark">NXT</div><div class="num">1</div></div>
</section>

<!-- Headline: solution -->
<section class="page" style="left:910px;top:36px">
  <div class="pg-title">HEADLINE HERE</div>
  <div class="content">
    <div class="h2">Solution</div>
    <div class="kicker">AI automated accounting</div>
    <div class="body"><p>Ledgra builds automation in stages on top of its current system to reach full automation thanks to the Ledgra AI. Ledgra AI automates every manual task performed by the user. It starts by connecting to all sources of accounting data such as bank accounts, credit card, webshop or document management systems (FileBox or Stora). Based on these dates, Ledgra AI creates bookings and generates financial reports. Finally, Ledgra AI features chat-like interface that allows users to communicate seamlessly with it, viewing it as a trusted advisor over time for all their accounting queries.</p></div>
    <div class="kicker">Blockchain software license or Token-as-a-License (TaaL)</div>
    <div class="body"><p>It is possible to create tokens on blockchain that represent software licenses, also known as Token-as-a-Licence (TaaL). Ledgra creates TaaL by using the Corvex official wallet which interacts with the Corvex blockchain. Upon purchase of TaaL, the token holder is free to transfer or sell TaaL using secondary market that is built directly over the blockchain, in our case, the Corvex marketplace. Ledgra checks the validity of a token against the blockchain ensuring that token holders have access to the software. TaaL make distribution and securisation of licenses easier for software developers. It also makes the management and resale of software license easier for software owners. All in all, TaaL has a higher value as a normal software license.</p></div>
    <div class="h2">Pre-ICO Token sale</div>
    <div class="body"><p>To realize this innovative vision, Ledgra is launching a pre-ICO in form of a token sale on Corvex blockchain. 20,000,000 tokens are available to purchase for the price of CHF 0.10 each during a 30-day period to be announced. Tokens represent Ledgra lifelong software licenses and by purchasing enough tokens, holders gain access to Ledgra software. 15,000 tokens give access to Ledgra invoicing or accounting. 20,000 tokens give access to both Ledgra accounting and invoicing. Future customers will still have the opportunity to buy directly yearly or monthly subscriptions to have access to Ledgra.</p></div>
    <div class="h2">Future plans</div>
    <div class="body"><p>A future ICO is planned between 18 and 24 months after the pre-ICO token sale. This offering will support the development of Ledgra into a fully decentralized, privacy-focused ecosystem of applications. The new model will reward each participant so that a new world with zero administrative tasks becomes reality.</p></div>
  </div>
  <div class="footer"><div class="url">www.website.com</div><div class="mark">NXT</div><div class="num">2</div></div>
</section>

<!-- Headline: two photos -->
<section class="page" style="left:47px;top:432px">
  <div class="pg-title">HEADLINE HERE</div>
  <div class="photo" role="img" aria-label="Hand drawing business icons on a board" style="position:absolute;left:26px;top:45px;width:89px;height:134px;background:linear-gradient(135deg,#c7d3de,#2b3846)"></div>
  <div class="photo" role="img" aria-label="Businessman seated thinking in an office" style="position:absolute;left:26px;top:202px;width:89px;height:118px;background:linear-gradient(135deg,#8aa3b5,#2c3136)"></div>
  <div style="position:absolute;left:126px;right:22px;top:45px">
    <div class="lead" style="font-size:5.4px;margin-bottom:5px">Ledgra's mission is to help and support the self-employed and small business owners with their administrative tasks so they can focus on what matters -- their business.</div>
    <div class="body">
      <p>Administrative tasks are cumbersome, time-consuming and often prevent small owners from focusing their time and energy on their business and their customers. They can also be extremely stressful and nerve-wracking for those attempting these tasks for the first time.</p>
      <p>At Ledgra, we envisage accounting for the self-employed and small business owners as being <span class="link">automated and decentralized</span></p>
      <p>Accounting can and should be done automatically. By connecting to all sources of accounting data such as bank accounts, payment systems, e-commerce websites, and invoicing systems, Ledgra AI automatically completes these tasks, which would take hours to do manually. Bookings are created automatically and fully completed. Financial statements are available within a couple of clicks, and after analysing your data, Ledgra AI will offer you tips to improve your financial stability.</p>
      <p>What may seem like a pipedream to the millions of self-employed who struggle with</p>
    </div>
    <div class="h2">The Ledgra model</div>
    <div class="body"><p>Ledgra is based on an innovative license model that uses Token-as-a-License (TaaL). The token represents lifelong software license for Ledgra solutions. The Pre-ICO token sales will enable Ledgra to complete its development of Ledgra AI to deliver fully automatic</p></div>
  </div>
  <div class="footer"><div class="url">www.website.com</div><div class="mark">NXT</div><div class="num">4</div></div>
</section>

<!-- Headline: banner photo -->
<section class="page" style="left:338px;top:432px">
  <div class="pg-title">HEADLINE HERE</div>
  <div role="img" aria-label="City highway interchange with orange light trails at night" style="position:absolute;left:28px;right:22px;top:45px;height:68px;background:linear-gradient(180deg,#6fa9cc 0%,#c98a3a 55%,#f2b23b 80%,#e07a1f 100%)"></div>
  <div class="content" style="top:118px">
    <div class="lead" style="margin-bottom:6px">Ledgra's mission is to help and support the self-employed and small business owners with</div>
    <div class="body">
      <p>Administrative tasks are cumbersome, time-consuming and often prevent small owners from focusing their time and energy on their business and their customers. They can also be extremely stressful and nerve-wracking for those attempting these tasks for the first time.</p>
      <p>At Ledgra, we envisage accounting for the self-employed and small business owners as being <span class="link">automated and decentralized</span></p>
    </div>
    <div style="border-top:0.5px solid var(--cyan-pale);margin-top:6px">
      <div style="height:10px"></div><div style="height:10px;background:var(--cyan-pale)"></div>
      <div style="height:10px"></div><div style="height:10px;background:var(--cyan-pale)"></div>
      <div style="height:10px"></div><div style="height:10px;background:var(--cyan-pale)"></div>
    </div>
    <div class="body" style="margin-top:8px">
      <p>Ledgra is based on an innovative license model that uses Token-as-a-License (TaaL). The token represents lifelong software license for Ledgra solutions. The Pre-ICO token sales will enable Ledgra to complete its development of Ledgra AI to deliver fully automatic bookkeeping.</p>
      <p>with leading edge business data access to ensure you have the best available data at your fingertips.</p>
    </div>
  </div>
  <div class="footer"><div class="url">www.website.com</div><div class="mark">NXT</div><div class="num">5</div></div>
</section>

<!-- Understanding of needs -->
<section class="page" style="left:628px;top:432px">
  <div class="pg-title">OUR UNDERSTANDING OF YOUR NEEDS</div>
  <div class="content" style="top:42px">
    <div class="h2">Implementation Estimate</div>
    <div class="body"><p>The bulk of the implementation costs will be defined by discovery. Based on similar CRM implementation projects, we feel expect that the CRM side will be somewhere between 200 and 300 hours, give or take. The wide swing in hours in phase one is related to the ill-defined nature of both the integration needs and our role in the integration project. Our focus in discovery (as mentioned above) will be to nail down those requirements and our role as it relates to what is needed to integrate the sites with the CRM.</p></div>
    <table class="grid" style="border-spacing:0;margin-top:6px">
      <tr class="head"><td></td><td></td><td></td></tr>
      <tr><td></td><td></td><td></td></tr><tr><td></td><td></td><td></td></tr>
      <tr><td></td><td></td><td></td></tr><tr><td></td><td></td><td></td></tr>
      <tr><td></td><td></td><td></td></tr><tr><td></td><td></td><td></td></tr>
      <tr><td></td><td></td><td></td></tr>
    </table>
    <table class="grid" style="border-spacing:0;margin-top:14px">
      <tr class="head"><td></td><td></td><td></td><td></td><td></td></tr>
      <tr><td></td><td></td><td></td><td></td><td></td></tr><tr><td></td><td></td><td></td><td></td><td></td></tr>
      <tr><td></td><td></td><td></td><td></td><td></td></tr><tr><td></td><td></td><td></td><td></td><td></td></tr>
      <tr><td></td><td></td><td></td><td></td><td></td></tr><tr><td></td><td></td><td></td><td></td><td></td></tr>
      <tr><td></td><td></td><td></td><td></td><td></td></tr>
    </table>
    <div class="h2" style="margin-top:12px">Implementation Estimate</div>
    <div class="body"><p>The bulk of the implementation costs will be defined by discovery. Based on similar CRM implementation projects, we feel expect that the CRM side will be somewhere between 200 and 300 hours, give or take. Our requirements and our role as it relates to what is needed to integrate the sites with the CRM.</p></div>
  </div>
  <div class="footer"><div class="url">www.website.com</div><div class="mark">NXT</div><div class="num">6</div></div>
</section>

<!-- Vision -->
<section class="page" style="left:910px;top:432px">
  <div class="pg-title">VISION</div>
  <div class="content">
    <div style="display:flex;height:23px;background:var(--slate)">
      <div style="width:26px;background:var(--cyan);display:flex;align-items:center;justify-content:center">
        <svg width="16" height="16" viewBox="0 0 16 16" aria-hidden="true"><circle cx="8" cy="8" r="6.5" fill="none" stroke="#fff" stroke-width="1.2"/><circle cx="8" cy="8" r="4" fill="none" stroke="#fff" stroke-width="1.2"/><circle cx="8" cy="8" r="1.5" fill="#fff"/><path d="M8 8 L14 2" stroke="#fff" stroke-width="1.2"/></svg>
      </div>
      <div style="flex:1;font-size:3.5px;line-height:1.4;color:#dfe6ec;padding:4px 6px">Ledgra's mission is to help and support the self-employed and small business owners with their administrative tasks so they can focus on what matters -- their business.</div>
    </div>
    <div class="body" style="margin-top:6px">
      <p>Administrative tasks are cumbersome, time-consuming and often prevent small owners from focusing their time and energy on their business and their customers. They can also be extremely stressful and nerve-wracking for those attempting these tasks for the first time.</p>
      <p style="text-align:center">At Ledgra, we envisage accounting for the self-employed and small business owners as being<br><span class="link">automated and decentralized</span></p>
      <p>Accounting can and should be done automatically. By connecting to all sources of accounting data such as bank accounts, payment systems, e-commerce websites, and invoicing systems, Ledgra AI automatically completes these tasks, which would take hours to do manually. Bookings are created automatically and fully completed. Financial statements are available within a couple of clicks, and after analysing your data, Ledgra AI will offer you tips to improve your financial stability.</p>
      <p>What may seem like a pipedream to the millions of self-employed who struggle with their admin, is already a reality. Now is the time to join Ledgra on its mission to transform the world of bookkeeping through the power of AI</p>
    </div>
    <div class="h2">The Ledgra model</div>
    <div class="body">
      <p>Ledgra is based on an innovative license model that uses Token-as-a-License (TaaL). The token represents lifelong software license for Ledgra solutions. The Pre-ICO token sales will enable Ledgra to complete its development of Ledgra AI to deliver fully automatic bookkeeping.</p>
      <p>The Pre-ICO token sale will also pave the way for a future Ledgra ICO. Ledgra will launch accounting on the blockchain and ensure your accounting data is comprehensive and private, but available everywhere within your preferred apps. It will empower you to manage your data as you see fit in a fully decentralized way. Furthermore, a new range of business apps will connect to Ledgra to provide you</p>
      <p>with leading edge business data access to ensure you have the best available data at your fingertips.</p>
      <p>Ledgra supports strong data ownership laws that truly protect individuals and ensure they have complete ownership of their data. Through decentralisation Ledgra helps to ensure you always have full ownership of your data to decide how it should be used.</p>
      <p>To find out more about the Ledgra AI project, and the Ledgra TaaL or if you are interested in purchasing Ledgra TaaL, please register with your email at <span class="link" style="text-decoration:underline">https://www.ledgra.example/ico</span> so we</p>
    </div>
  </div>
  <div class="footer"><div class="url">www.website.com</div><div class="mark">NXT</div><div class="num">4</div></div>
</section>

<!-- Budget and timeframe -->
<section class="page" style="left:47px;top:818px">
  <div class="pg-title">BUDGET AND TIMEFRAME</div>
  <div class="content" style="top:42px">
    <div class="h2">Implementation Estimate</div>
    <div class="body"><p>The bulk of the implementation costs will be defined by discovery. Based on similar CRM implementation projects, we feel expect that the CRM side will be somewhere between 200 and 300 hours, give or take. The wide swing in hours in phase one is related to the ill-defined nature of both the integration needs and our role in the integration project. Our focus in discovery (as mentioned above) will be to nail down those requirements and our role as it relates to what is needed to integrate the sites with the CRM.</p></div>
    <table class="data" style="margin-top:3px">
      <tr><th style="width:108px">Task</th><th>Hours</th><th>Cost</th></tr>
      <tr><td>Discovery</td><td class="c">40</td><td class="c">$8,000</td></tr>
      <tr class="sub"><td colspan="3">Phase 1</td></tr>
      <tr><td>Discovery</td><td class="c">20-40</td><td class="c">$8,000</td></tr>
      <tr><td>Discovery</td><td class="c">20-40</td><td class="c">$8,000</td></tr>
      <tr><td>Discovery</td><td class="c">20-40</td><td class="c">$8,000</td></tr>
      <tr class="total"><td>Total Phase 1</td><td class="c">80-240</td><td class="c">$16,800-40,000</td></tr>
      <tr class="sub"><td colspan="3">Phase 2</td></tr>
      <tr><td>Discovery</td><td class="c">20-40</td><td class="c">$8,000</td></tr>
      <tr class="total"><td>Total Phase 2</td><td class="c">80-240</td><td class="c">$16,800-40,000</td></tr>
      <tr class="grand"><td>Total Estimated Implementation Cost</td><td class="c">220-480</td><td class="c">$44,000-96,000</td></tr>
    </table>
    <div class="h2" style="margin-top:12px">Project Timeline</div>
    <div class="body"><p>Based on the information we have at our disposal, the March 21st launch date doesn't seem a realistic goal to get both the work done needed to provide the foundation for the future CRM instance and the integration given the state of apparent flux of the requirements. That said, we feel it prudent to proceed with discovery before committing to or pushing that date. We are currently estimating that the first phase will take somewhere between 7 and 12 weeks (including discovery) to complete.</p></div>
    <table class="data" style="margin-top:5px">
      <tr><th style="width:128px">Task</th><th>Weeks to Complete</th></tr>
      <tr><td>Discovery</td><td class="c">1-2</td></tr>
      <tr><td>Phase 1</td><td class="c">6-10</td></tr>
      <tr><td>Phase 2</td><td class="c">8-12</td></tr>
      <tr class="total"><td>Total Number of Weeks</td><td class="c"></td></tr>
    </table>
  </div>
  <div class="footer"><div class="url">www.website.com</div><div class="mark">NXT</div><div class="num">7</div></div>
</section>

<!-- Back cover -->
<section class="page" style="left:338px;top:818px">
  <div role="img" aria-label="Faint perspective pattern of pale blue tiles" style="position:absolute;left:0;right:0;top:80px;height:200px;background:radial-gradient(ellipse at 50% 55%,#ffffff 0%,#e6f2fa 35%,#b9dcf1 70%,#ffffff 100%)"></div>
  <div style="position:absolute;left:46px;top:298px;display:flex;align-items:center;gap:6px">
    <div style="font-size:15px;font-weight:900;color:var(--slate)">NXT</div>
    <div style="width:1px;height:16px;background:var(--cyan)"></div>
    <div style="font-size:2.8px;line-height:1.7;color:var(--ink)">
      <div><svg width="3" height="3" viewBox="0 0 4 4"><circle cx="2" cy="2" r="2" fill="var(--cyan)"/></svg> 000-555-0142 Ext 210</div>
      <div><svg width="3" height="3" viewBox="0 0 4 4"><circle cx="2" cy="2" r="2" fill="var(--cyan)"/></svg> hello@nxtdomain.com</div>
      <div><svg width="3" height="3" viewBox="0 0 4 4"><circle cx="2" cy="2" r="2" fill="var(--cyan)"/></svg> www.nxtdomain.com</div>
    </div>
    <div style="width:0.5px;height:16px;background:#bbb"></div>
    <div style="font-size:2.8px;line-height:1.7;color:var(--ink)">210, 480 Harbour Line Street<br>Northbay, Coastal Province 1234</div>
  </div>
</section>

</body>
</html>
```